依頼詳細
ダンスの発表会は
2年に1回 ホールを借りて発表会を行っています。

今回は2024年 4月14日に開催いたします。
今回で 7回目になります。

発表会の年齢層は 幼稚園から 中学3年生までになります。

発表会のコンセプトは
sub Title: Keep a Warm Glow(意味:輝く笑顔)
Main :Life is fun(意味:全力で楽しむ!)

Keep a Warm Glow は、毎年同じテーマです。
Life is fun はコロナのようにいつ何が起こるかわからないので、今を全力で楽しむという意味をこめて
記載項目
記載内容は下記のとおりです。

*全て 英語で記載
*大文字、小文字に関してはお任せします。

KRN のロゴ

7th

2024.4.14 Sun

1st Open 10:00 Start 10:30
2nd Open 14:30 Start 15:00

Location Toreda Geijutsu Center Hanayuri Hall

Keep a Warm Glow
Life is fun
サイズ
A4
ページ数
片面
希望イメージ
シンプル 複雑
単色 カラフル
暗い 明るい
日常 高級
遊び心 厳粛
未来的 伝統的
女性的 男性的
希望する色
紫系
納品ファイル
• イラストレーター形式 (.ai)
生成AI使用可否
納品物の制作に生成AIの使用がOK
追加で テンプレートページA3 × 3ページ A4 × 1ページ

は別途費用を お支払いいたします。
■ 選んだ理由

最初に希望していた通りのデザインでした。素敵なデザインありがとうございます。

■ 提案者全員のお礼・コメント

本当にたくさんのご提案いただきありがとうございます!
感謝いたします。

```html
<!DOCTYPE html>
<html lang="en">
<head>
<meta charset="UTF-8">
<title>Life is fun — KRN Cheer &amp; Dance 7th Recital</title>
<link rel="stylesheet" href="https://fonts.googleapis.com/css2?family=Playfair+Display:ital,wght@1,700;1,800&family=Montserrat:wght@600;700;800&display=swap">
<style>
  :root{
    --bg:#a08fbf;
    --white:#ffffff;
    --ink-soft:#f4eefb;
    --holo-a:#ffd6ec;
    --holo-b:#ffffff;
    --holo-c:#c9e6ff;
    --holo-d:#e6d3ff;
    --holo-e:#fbe3f3;
    --line:#f3ecfb;
  }
  *{margin:0;padding:0;box-sizing:border-box}
  html,body{width:849px;height:1200px;overflow:hidden;background:var(--bg)}
  .poster{
    position:relative;width:849px;height:1200px;background:var(--bg);
    font-family:"Montserrat",sans-serif;color:var(--white);overflow:hidden;
  }
  .holo{
    background:linear-gradient(100deg,var(--holo-a) 0%,var(--holo-b) 22%,var(--holo-c) 45%,var(--holo-d) 65%,var(--holo-b) 82%,var(--holo-e) 100%);
    -webkit-background-clip:text;background-clip:text;color:transparent;
  }
  .subtitle{
    position:absolute;top:30px;left:0;width:100%;text-align:center;
    font-family:"Playfair Display",serif;font-style:italic;font-weight:700;
    font-size:38px;letter-spacing:1px;color:var(--white);
  }
  .subtitle .slash{font-style:normal;font-weight:400;margin:0 14px}
  .main-title{
    position:absolute;top:78px;left:0;width:100%;text-align:center;
    font-family:"Playfair Display",serif;font-style:italic;font-weight:800;
    font-size:112px;line-height:1.1;letter-spacing:-1px;
  }
  .frame{position:absolute;left:0;top:0}
  .edition{
    position:absolute;left:148px;top:215px;width:70px;
    text-align:center;font-weight:800;font-size:30px;
  }
  .edition sup{font-size:17px;vertical-align:10px;margin-left:1px}
  .brand{
    position:absolute;left:119px;top:280px;width:611px;text-align:center;
    font-weight:800;
  }
  .brand-name{font-size:168px;line-height:1;letter-spacing:8px}
  .brand-sub{font-size:50px;letter-spacing:4px;margin-top:8px}
  .date{
    position:absolute;top:700px;left:0;width:100%;text-align:center;
    font-weight:700;font-size:74px;letter-spacing:1px;
  }
  .sessions{
    position:absolute;top:806px;left:0;width:100%;
    display:flex;justify-content:center;gap:46px;
  }
  .session{display:flex;align-items:center;gap:16px}
  .session-badge{width:100px;height:100px;position:relative}
  .session-badge svg{position:absolute;inset:0}
  .session-badge span{
    position:absolute;inset:0;display:flex;align-items:center;justify-content:center;
    font-weight:800;font-size:30px;color:var(--white);
  }
  .session-badge sup{font-size:16px;vertical-align:10px}
  .session-times{font-weight:700;font-size:32px;line-height:1.3;color:var(--white)}
  .location{
    position:absolute;top:988px;left:0;width:100%;
    display:flex;justify-content:center;align-items:center;gap:14px;
  }
  .location-label{font-weight:700;font-size:27px;color:var(--white)}
  .location-place{
    padding:6px 18px;border-radius:8px;
    background:linear-gradient(100deg,#fde3f2,#ffffff 40%,#d7ecff 70%,#eadcff);
    font-weight:700;font-size:25px;color:#9b88bd;
  }
</style>
</head>
<body>
<main class="poster">
  <p class="subtitle"><span class="slash">\</span>Keep a Warm Glow<span class="slash">/</span></p>
  <h1 class="main-title holo">Life is fun</h1>

  <svg class="frame" width="849" height="1200" viewBox="0 0 849 1200" aria-hidden="true">
    <defs>
      <linearGradient id="holoStroke" x1="0" y1="0" x2="1" y2="1">
        <stop offset="0" stop-color="#ffd6ec"/>
        <stop offset="0.35" stop-color="#ffffff"/>
        <stop offset="0.6" stop-color="#c9e6ff"/>
        <stop offset="1" stop-color="#f2dcff"/>
      </linearGradient>
    </defs>
    <path d="M230 228 H705 Q730 228 730 253 V485 Q730 510 705 510 H144 Q119 510 119 485 V253 Q119 228 144 228"
          fill="none" stroke="url(#holoStroke)" stroke-width="4"/>
    <rect x="140" y="196" width="86" height="84" rx="14" fill="none" stroke="url(#holoStroke)" stroke-width="4"/>
  </svg>
  <p class="edition holo">7<sup>th</sup></p>

  <div class="brand">
    <p class="brand-name holo">KRN</p>
    <p class="brand-sub holo">CHEER &amp; DANCE</p>
  </div>

  <p class="date holo">2024.4.14 Sun</p>

  <section class="sessions">
    <div class="session">
      <div class="session-badge">
        <svg width="100" height="100" viewBox="0 0 100 100" aria-hidden="true">
          <circle cx="50" cy="50" r="45" fill="none" stroke="var(--line)" stroke-width="3" stroke-dasharray="6 5"/>
        </svg>
        <span>1<sup>st</sup></span>
      </div>
      <p class="session-times">Open 10:00<br>Start 10:30</p>
    </div>
    <div class="session">
      <div class="session-badge">
        <svg width="100" height="100" viewBox="0 0 100 100" aria-hidden="true">
          <circle cx="50" cy="50" r="45" fill="none" stroke="var(--line)" stroke-width="3" stroke-dasharray="6 5"/>
        </svg>
        <span>2<sup>nd</sup></span>
      </div>
      <p class="session-times">Open 14:30<br>Start 15:00</p>
    </div>
  </section>

  <section class="location">
    <span class="location-label">Location</span>
    <span class="location-place">Toreda Geijutsu Center Hanayuri Hall</span>
  </section>
</main>
</body>
</html>
```